Business Card design for shipping company 'FARNHOLT MARITIME LTD'

Classic / traditional business card in black Garamond / Times New Roman or similar text for a shipping / marine transport company, containing the following information:

QUOTE

FARNHOLT MARITIME LTD

PETER CALLOWAY FICS

T: +44 7923 615087
E: vessels@farnholt-mar.com

UNQUOTE

Target Market(s)

Marine / Shipping industry

Contact Information for Business Card

FARNHOLT MARITIME LTD PETER CALLOWAY FICS T: +44 7923 615087 E: vessels@farnholt-mar.com

Font styles to use
Serif

Colors

Designer to choose colors to be used in the design.

Requirements
Must have
• Garamond / Times New Roman or similar text in black colour

```html
<!DOCTYPE html>
<html lang="en">
<head>
<meta charset="utf-8">
<title>Farnholt Maritime Ltd – Business Card</title>
<link rel="stylesheet" href="https://fonts.googleapis.com/css2?family=Cormorant+Garamond:ital,wght@0,500;1,600&display=swap">
<style>
  :root {
    --backdrop: #1c1c1c;
    --card-black: #141414;
    --card-white: #f7f7f5;
    --ink-black: #161616;
    --ink-white: #f2f2f2;
    --wave-dark-a: #1e1e1e;
    --wave-dark-b: #2b2b2b;
    --wave-light-a: #e9e9e7;
    --wave-light-b: #dcdcda;
  }
  * { box-sizing: border-box; margin: 0; padding: 0; }
  html, body {
    width: 1200px;
    height: 852px;
    overflow: hidden;
    background: var(--backdrop);
  }
  .stage {
    width: 1200px;
    height: 852px;
    display: flex;
    align-items: center;
    justify-content: center;
    gap: 40px;
  }
  .card {
    position: relative;
    width: 540px;
    height: 310px;
    border-radius: 22px;
    overflow: hidden;
    box-shadow: 0 10px 28px rgba(0,0,0,0.55);
  }
  .card--front { background: var(--card-black); }
  .card--back { background: var(--card-white); }

  .wave-pattern {
    position: absolute;
    display: block;
  }
  .card--front .wave-pattern {
    inset: 0;
    background: linear-gradient(160deg, var(--wave-dark-a), var(--wave-dark-b) 50%, var(--wave-dark-a));
  }
  .card--back .wave-pattern {
    left: 330px;
    top: 22px;
    width: 180px;
    height: 198px;
    border-radius: 6px;
    background: linear-gradient(160deg, var(--wave-light-a), var(--wave-light-b));
  }

  .company-name {
    position: absolute;
    left: 0;
    right: 0;
    top: 50%;
    transform: translateY(-50%);
    text-align: center;
    font-family: "Cormorant Garamond", "Times New Roman", serif;
    font-weight: 500;
    font-size: 34px;
    letter-spacing: 0.08em;
    color: var(--ink-white);
  }

  .contact {
    position: absolute;
    left: 36px;
    bottom: 30px;
    font-family: "Cormorant Garamond", "Times New Roman", serif;
    color: var(--ink-black);
  }
  .contact__name {
    font-style: italic;
    font-weight: 600;
    font-size: 19px;
    margin-bottom: 8px;
  }
  .contact__line {
    font-weight: 500;
    font-size: 14.5px;
    line-height: 1.4;
  }
</style>
</head>
<body>
  <main class="stage">
    <section class="card card--front" aria-label="Card front">
      <div class="wave-pattern" role="img" aria-label="Fine wavy line pattern across the card"></div>
      <h1 class="company-name">FARNHOLT MARITIME LTD</h1>
    </section>

    <section class="card card--back" aria-label="Card back">
      <div class="wave-pattern" role="img" aria-label="Column of wavy lines suggesting water"></div>
      <div class="contact">
        <p class="contact__name">Peter Calloway Fics</p>
        <p class="contact__line">T: +44 7923 615087</p>
        <p class="contact__line">E: vessels@farnholt-mar.com</p>
      </div>
    </section>
  </main>
</body>
</html>
```